Energy Healing for pregnant women postcard

I am an intuitive energy healer specializing in the care of pregnant women and their babies. I have an existing logo that is attached that should be placed on the card,sizing is at your discretion, recolor as needed. The message of the card should be one that conveys tranquility, growth, life and light. Images of pregnancy and motherhood could also fit well on the card, but that is not required if the preceding messages can be conveyed through other imagery. Also on the card, the following should appear: (company name and tag line)Positivity & JoyHealing the mind, body, spirit and soul with Energy provided to all living things by the Universe. Space should be left for my name and credentials on the front, while the address space on the back will be used for more contact information. Opposite the address block on the back, please leave room for a text box that will include benefits of the services. About 2"x3" should suffice.

Target Market(s)

Pregnant women and newly post-partum women

Industry/Entity Type

Health And Wellness

Font styles to use
Script

Colors
b05ba4
b768aa
d3a5cc
ecdaeb
e7f5f8
cfdeed
cee9f5
85cae6

Requirements
Must have
• Company logo. Company name. Tag line. Individual name and certifications
Nice to have
• Pictures or images that convey peace, tranquility healing and growth.
Should not have
• Anything harsh.

```html
<!DOCTYPE html>
<html lang="en">
<head>
<meta charset="utf-8">
<title>Harbor &amp; Wren — Energy Healing Postcard</title>
<link rel="stylesheet" href="https://fonts.googleapis.com/css2?family=Kurale&family=Delius&family=Nunito:wght@700;800&display=swap">
<style>
  :root {
    --bg-top: #fbe4ea;
    --bg-bottom: #f6cdd7;
    --green: #3f7a5c;
    --green-soft: #5d8f70;
    --coral: #e0566b;
    --amber: #e9a14b;
    --teal-light: #8fd0cf;
    --art-pink: rgba(244, 169, 182, 0.55);
    --art-peach: rgba(247, 197, 143, 0.45);
    --art-mint: rgba(140, 201, 184, 0.35);
    --petal: rgba(255, 236, 228, 0.75);
    --petal-core: rgba(246, 200, 190, 0.6);
  }
  * { margin: 0; padding: 0; box-sizing: border-box; }
  html, body { width: 1200px; height: 858px; overflow: hidden; }
  body { background: #fff; }
  .postcard {
    position: relative;
    width: 1200px;
    height: 858px;
    overflow: hidden;
    background: radial-gradient(ellipse at 65% 40%, #fdf0f3 0%, var(--bg-top) 45%, var(--bg-bottom) 100%);
  }
  .illustration-area {
    position: absolute;
    left: 0; top: 0;
    width: 380px; height: 858px;
    background:
      linear-gradient(90deg, rgba(251, 228, 234, 0) 70%, var(--bg-top) 100%),
      linear-gradient(180deg, var(--art-pink) 0%, var(--art-peach) 50%, var(--art-mint) 100%);
  }
  .bloom-decor {
    position: absolute;
    left: 640px; top: 300px;
    width: 560px; height: 440px;
  }
  .brand {
    position: absolute;
    left: 408px; top: 70px;
    width: 120px;
    display: flex; align-items: center; gap: 8px;
  }
  .brand-dot {
    flex: none;
    width: 24px; height: 24px; border-radius: 50%;
    background: var(--green-soft);
  }
  .brand-name {
    font-family: "Kurale", serif;
    font-size: 17px;
    line-height: 20px;
    color: var(--green-soft);
  }
  .title {
    position: absolute;
    left: 540px; top: 58px;
    font-family: "Kurale", serif;
    font-size: 64px;
    font-weight: 400;
    color: var(--green);
    letter-spacing: 1px;
    white-space: nowrap;
  }
  .tagline {
    position: absolute;
    left: 412px; top: 170px;
    width: 770px;
    font-family: "Delius", cursive;
    font-size: 34px;
    line-height: 46px;
    color: var(--coral);
  }
  .benefit {
    position: absolute;
    font-family: "Delius", cursive;
    font-size: 30px;
    white-space: nowrap;
  }
  .benefit--amber { color: var(--amber); }
  .benefit--green { color: var(--green); }
  .benefit--coral { color: var(--coral); }
  .benefit--teal { color: var(--teal-light); }
  .practitioner {
    position: absolute;
    text-align: right;
    font-family: "Nunito", sans-serif;
    color: var(--green);
    white-space: nowrap;
  }
  .practitioner-name { right: 86px; top: 738px; font-size: 37px; font-weight: 800; }
  .practitioner-credentials { right: 48px; top: 788px; font-size: 27px; font-weight: 700; }
</style>
</head>
<body>
<main class="postcard">
  <div class="illustration-area" role="img" aria-label="Illustration of a pregnant woman in profile, formed from pastel flowers, hearts, leaves and music notes"></div>

  <svg class="bloom-decor" viewBox="0 0 560 440" role="img" aria-label="Faint pale flower blossoms in the background">
    <circle cx="260" cy="80" r="85" fill="var(--petal)"/>
    <circle cx="260" cy="80" r="30" fill="var(--petal-core)"/>
    <circle cx="440" cy="340" r="80" fill="var(--petal)"/>
    <circle cx="440" cy="340" r="28" fill="var(--petal-core)"/>
    <circle cx="40" cy="200" r="60" fill="var(--petal)"/>
  </svg>

  <div class="brand">
    <span class="brand-dot"></span>
    <span class="brand-name">Harbor &amp; Wren</span>
  </div>

  <h1 class="title">Harbor &amp; Wren</h1>

  <p class="tagline">Healing the mind, body, spirit and soul<br>with Energy provided to all living things<br>by the Universe</p>

  <span class="benefit benefit--amber" style="left:576px; top:390px;">Promote balance</span>
  <span class="benefit benefit--green" style="left:882px; top:390px;">Decrease stress</span>
  <span class="benefit benefit--coral" style="left:622px; top:436px;">Promote feelings of wellbeing</span>
  <span class="benefit benefit--green" style="left:522px; top:486px;">Decrease anxiety</span>
  <span class="benefit benefit--amber" style="left:940px; top:486px;">Deep relaxation</span>
  <span class="benefit benefit--teal" style="left:686px; top:534px;">Decrease discomforts</span>
  <span class="benefit benefit--coral" style="left:524px; top:580px;">Relieve physical discomforts of pregnancy</span>

  <p class="practitioner practitioner-name">Claire M. Holloway, MSN, RCMT</p>
  <p class="practitioner practitioner-credentials">Reiki Master Teacher, Archangelic Light Master Teacher</p>
</main>
</body>
</html>
```